Layout for site fence advertising - length approx. 250 cm x 125 cm

The advertising will later be printed on a PVC film and used for events or on sports fields.

Main services :
Your regional contact at
Real estate and business financing
independent insurance advice

```html
<!DOCTYPE html>
<html lang="de">
<head>
<meta charset="utf-8">
<title>RW Finanzpartner GmbH – Bauzaunbanner</title>
<link rel="stylesheet" href="https://fonts.googleapis.com/css2?family=Poppins:wght@500;600;700&display=swap">
<style>
  :root {
    --stage: #e4e4e6;
    --paper: #ffffff;
    --brand-blue: #2a5aab;
    --ink-grey: #5f5f61;
    --photo-dark: #3a2a26;
    --photo-mid: #6b4a3f;
    --photo-light: #b9a69c;
  }
  * { margin: 0; padding: 0; box-sizing: border-box; }
  html, body {
    width: 1200px;
    height: 763px;
    overflow: hidden;
    background: var(--stage);
    font-family: "Poppins", Arial, sans-serif;
  }
  .banner {
    position: absolute;
    left: 101px;
    top: 137px;
    width: 1040px;
    height: 519px;
    background: var(--paper);
    overflow: hidden;
    box-shadow: 3px 3px 6px rgba(0, 0, 0, 0.18);
  }
  .banner-art {
    position: absolute;
    inset: 0;
    width: 1040px;
    height: 519px;
  }
  .brand {
    position: absolute;
    left: 49px;
    top: 46px;
    height: 126px;
    display: flex;
    align-items: center;
  }
  .brand-circle {
    width: 122px;
    height: 122px;
    border: 3px solid var(--brand-blue);
    border-radius: 50%;
    margin-right: 22px;
  }
  .brand-divider {
    width: 3px;
    height: 126px;
    background: var(--ink-grey);
    margin-right: 10px;
  }
  .brand-name {
    font-weight: 600;
    font-size: 24px;
    line-height: 1.1;
    color: var(--brand-blue);
    white-space: nowrap;
  }
  .brand-tagline {
    font-weight: 500;
    font-size: 17px;
    line-height: 1.2;
    color: var(--ink-grey);
    margin-top: 6px;
    white-space: nowrap;
  }
  .services {
    position: absolute;
    left: 50px;
    top: 217px;
    color: var(--paper);
    text-transform: uppercase;
  }
  .services-title {
    font-weight: 700;
    font-size: 32px;
    line-height: 40px;
    letter-spacing: -0.3px;
    margin-bottom: 2px;
  }
  .services-list { list-style: none; }
  .services-list li {
    font-weight: 700;
    font-size: 20px;
    line-height: 35.5px;
    letter-spacing: -0.1px;
    white-space: nowrap;
  }
</style>
</head>
<body>
  <div class="banner">
    <svg class="banner-art" viewBox="0 0 1040 519" xmlns="http://www.w3.org/2000/svg">
      <defs>
        <linearGradient id="portrait-tone" x1="0" y1="0" x2="1" y2="1">
          <stop offset="0" stop-color="#3b2724"/>
          <stop offset="0.45" stop-color="#6e4e43"/>
          <stop offset="0.75" stop-color="#8c6f63"/>
          <stop offset="1" stop-color="#2e2a33"/>
        </linearGradient>
        <linearGradient id="portrait-fade" x1="0" y1="0" x2="1" y2="0">
          <stop offset="0" stop-color="#ffffff" stop-opacity="0.9"/>
          <stop offset="1" stop-color="#ffffff" stop-opacity="0"/>
        </linearGradient>
        <clipPath id="white-field">
          <path d="M0,0 H494 A322,322 0 0 1 497,519 H0 Z"/>
        </clipPath>
      </defs>

      <g role="img" aria-label="Porträtfoto des Beraters im dunklen Sakko vor warmem Holzhintergrund">
        <rect x="480" y="0" width="560" height="519" fill="url(#portrait-tone)"/>
        <rect x="480" y="380" width="150" height="139" fill="url(#portrait-fade)"/>
      </g>

      <path class="white-field" d="M0,0 H494 A322,322 0 0 1 497,519 H0 Z" fill="#ffffff"/>

      <rect class="service-band" x="0" y="206" width="700" height="183" fill="#2a5aab" clip-path="url(#white-field)"/>

      <circle class="corner-arc" cx="45" cy="568" r="114" fill="none" stroke="#5f5f61" stroke-width="3"/>
    </svg>

    <div class="brand">
      <div class="brand-circle"></div>
      <div class="brand-divider"></div>
      <div class="brand-text">
        <div class="brand-name">RW Finanzpartner GmbH</div>
        <div class="brand-tagline">Finanzieren, Versichern, Vorsorgen</div>
      </div>
    </div>

    <div class="services">
      <h1 class="services-title">Hauptleistungen :</h1>
      <ul class="services-list">
        <li>Ihr regionaler Ansprechpartner unter</li>
        <li>Immobilien- und Unternehmensfinanzierung</li>
        <li>Unabhängige Versicherungsberatung</li>
      </ul>
    </div>
  </div>
</body>
</html>
```